Perfume packaging design

We are a company producing perfumery and deodorants in the upper mass market segment (semi-selective). We need a packaging design for our new fragrance for women called Moon Petal. You will find attached a picture of the chosen bottle and cap along with specification.

The fragrance is modern and delicate. It is sweet with floral accent and notes of mandarin, rose, peach.

Suitable for evening perfume as well as casual daily.

Looking for:
1. logo - "Moon Petal" on bottle and packaging
2. Color of the perfume
3. Design of the carton box

Product is 100ml eau de perfume for women.

Target Market(s)

Target market is Eastern Europe and middle east

Women
Age 30-45
Price range - semi-selective
Sales channels - perfumeries, drug stores and online

Industry/Entity Type

It Company

Requirements
Must have
• Packaging - carton
Perfume should be colored
Embosing
Nice to have
• Golden hot stamping or other golden element

```html
<!DOCTYPE html>
<html lang="en">
<head>
<meta charset="utf-8">
<title>Moon Petal – Label</title>
<link rel="stylesheet" href="https://fonts.googleapis.com/css2?family=Parisienne&display=swap">
<style>
  :root {
    --canvas-bg: #1a1a1c;
    --label-black: #000000;
    --gold-core: #e9c349;
    --gold-mid: #b8861f;
    --gold-deep: #5a3d0a;
    --name-gold: #c89a3a;
  }
  html, body {
    margin: 0;
    padding: 0;
    width: 1200px;
    height: 900px;
    overflow: hidden;
    background: var(--canvas-bg);
  }
  .canvas {
    position: relative;
    width: 1200px;
    height: 900px;
    display: flex;
    align-items: center;
    justify-content: center;
  }
  .label {
    position: relative;
    width: 850px;
    height: 686px;
    background: var(--label-black);
    overflow: hidden;
  }
  .label__glitter-cloud {
    position: absolute;
    left: 50%;
    top: 50%;
    width: 700px;
    height: 420px;
    transform: translate(-50%, -52%);
    border-radius: 50%;
    background: radial-gradient(ellipse at center,
      var(--gold-core) 0%,
      var(--gold-mid) 38%,
      var(--gold-deep) 62%,
      rgba(0,0,0,0) 74%);
    filter: blur(6px);
  }
  .label__name {
    position: absolute;
    left: 0;
    right: 0;
    top: 50%;
    transform: translateY(-58%);
    margin: 0;
    text-align: center;
    font-family: "Parisienne", cursive;
    font-weight: 400;
    font-size: 128px;
    line-height: 1;
    color: var(--name-gold);
  }
</style>
</head>
<body>
  <main class="canvas">
    <section class="label">
      <div class="label__glitter-cloud" role="img" aria-label="Cloud of scattered golden glitter on black"></div>
      <h1 class="label__name">Moon Petal</h1>
    </section>
  </main>
</body>
</html>
```